Health and Wellness Company Needs Brochure to Describe New Exercise Class Offering

We need a brochure to help clients better understand our new service offering. We are a Portland, OR based health and wellness company called 'stride haven studio'. We provide instruction in group exercise classes designed to reduce pain and improve movement. Similar to physical therapy but with the teaching environment similar to a yoga studio.

Please see attached word document that outlines the sections that should be included in the brochure.

We would like to see the color orange throughout the brochure as that color reflects vitality and energy. Our logo should be included in the design. Our slogan is "Feel Better. Move Better. Live Better." Go to our website www.stridehavenstudio.example for more information.

Target Market(s)

Exercise conscious, recreational athletes who are proactive about their health and well-being and looking for an alternative to physical therapy.

Industry/Entity Type

Health And Wellness

Font styles to use
Sans Serif

Requirements
Must have
• Logo placed strategically throughout the brochure.
• A trifold brochure.
Should not have
• I'd like to avoid the standard 3 panel design. Instead I'd like to see the design spread out over the page with 3 sections arbitrarily created by the designer that doesn't follow the fold pattern of the trifold brochure.

```html
<!DOCTYPE html>
<html lang="en">
<head>
<meta charset="utf-8">
<title>Stride Haven Studio – Trifold Brochure</title>
<link rel="stylesheet" href="https://fonts.googleapis.com/css2?family=Didact+Gothic&family=Mulish:wght@700;800&display=swap">
<style>
  :root {
    --orange: #f7931e;
    --orange-deep: #ef7f12;
    --purple: #5b5bb0;
    --ink: #1e1e1e;
    --paper: #ffffff;
    --paper-shade: #ececec;
    --backdrop: #2b2b2b;
  }
  * { margin: 0; padding: 0; box-sizing: border-box; }
  html, body { width: 1200px; height: 850px; overflow: hidden; background: var(--backdrop); }
  .canvas { position: relative; width: 1200px; height: 850px; font-family: "Didact Gothic", sans-serif; }
  .brochure { position: absolute; left: 75px; top: 52px; width: 1050px; height: 745px; background: var(--paper); overflow: hidden; }
  .artwork { position: absolute; inset: 0; }
  .panel { position: absolute; top: 0; height: 745px; width: 350px; }
  .panel-left { left: 0; }
  .panel-middle { left: 350px; text-align: center; }
  .panel-right { left: 700px; text-align: center; }

  .posture-title { position: absolute; left: 35px; top: 41px; color: var(--purple); font-size: 17px; line-height: 22px; }
  .posture-copy { position: absolute; left: 35px; top: 109px; width: 270px; font-size: 10.6px; line-height: 13.6px; color: var(--ink); text-align: justify; }
  .posture-copy p { margin-bottom: 13px; }

  .seminar-badge { position: absolute; left: 27px; top: 48px; width: 296px; height: 148px; background: var(--orange); border-radius: 10px; box-shadow: 0 6px 8px rgba(0,0,0,.25); padding: 8px; }
  .seminar-badge-inner { width: 100%; height: 100%; border: 1.5px dashed rgba(255,255,255,.85); border-radius: 6px; padding-top: 8px; font-family: "Mulish", sans-serif; font-weight: 800; }
  .seminar-free { color: var(--paper); font-size: 44px; line-height: 46px; }
  .seminar-name { color: var(--purple); font-size: 29px; line-height: 31px; }
  .slogan { position: absolute; left: 0; width: 350px; top: 230px; color: var(--purple); font-size: 27px; line-height: 36px; }
  .divider { position: absolute; left: 95px; top: 366px; width: 160px; height: 1px; background: linear-gradient(90deg, transparent, #c9a46a, transparent); }
  .seminar-copy { position: absolute; left: 50px; width: 250px; top: 401px; font-size: 15.5px; line-height: 21px; color: var(--ink); }
  .highlight { color: var(--orange); font-family: "Mulish", sans-serif; font-weight: 800; }
  .reserve { position: absolute; left: 0; width: 350px; top: 561px; font-size: 15.5px; line-height: 21px; color: var(--ink); }
  .reserve .url { color: var(--orange); }
  .footer-brand { position: absolute; left: 0; width: 350px; top: 702px; display: flex; justify-content: center; align-items: center; gap: 8px; color: var(--paper); font-size: 21px; }

  .brand { display: inline-flex; align-items: center; gap: 9px; }
  .brand-square { width: 20px; height: 20px; border: 3px solid currentColor; }
  .header-brand { position: absolute; left: 0; width: 350px; top: 82px; display: flex; justify-content: center; align-items: center; gap: 9px; color: var(--purple); font-size: 25px; }
  .cover-headline { position: absolute; left: 0; width: 350px; top: 455px; color: var(--paper); font-size: 29px; line-height: 34px; text-shadow: 0 1px 3px rgba(0,0,0,.35); }
</style>
</head>
<body>
<div class="canvas">
  <div class="brochure">
    <svg class="artwork" width="1050" height="745" viewBox="0 0 1050 745">
      <defs>
        <linearGradient id="studioTone" x1="0" y1="0" x2="1" y2="1">
          <stop offset="0" stop-color="#eee6e4"/>
          <stop offset="0.5" stop-color="#f8f5f3"/>
          <stop offset="1" stop-color="#e6dcd8"/>
        </linearGradient>
        <linearGradient id="middleTone" x1="0" y1="0" x2="1" y2="0">
          <stop offset="0" stop-color="#e9e9e9"/>
          <stop offset="0.25" stop-color="#ffffff"/>
          <stop offset="1" stop-color="#f4f4f4"/>
        </linearGradient>
        <linearGradient id="roadTone" x1="0" y1="0" x2="0" y2="1">
          <stop offset="0" stop-color="#b9a98a"/>
          <stop offset="0.3" stop-color="#8b8a78"/>
          <stop offset="0.6" stop-color="#46484e"/>
          <stop offset="1" stop-color="#2c2d33"/>
        </linearGradient>
        <radialGradient id="mirrorTone" cx="0.5" cy="0.5" r="0.6">
          <stop offset="0" stop-color="#c9a590"/>
          <stop offset="1" stop-color="#6d5a52"/>
        </radialGradient>
        <radialGradient id="classTone" cx="0.5" cy="0.5" r="0.6">
          <stop offset="0" stop-color="#e4d6c8"/>
          <stop offset="1" stop-color="#9f8f84"/>
        </radialGradient>
      </defs>

      <rect class="panel-middle-bg" x="350" y="0" width="350" height="745" fill="url(#middleTone)"/>
      <rect role="img" aria-label="Soft, faded photo of a woman checking her posture in a bright studio" x="0" y="0" width="350" height="600" fill="url(#studioTone)"/>

      <!-- lower sweep across the spread -->
      <path class="sweep-purple" d="M0,420 C120,470 260,580 420,625 C560,662 700,650 780,625 C880,595 980,565 1050,548 L1050,575 C960,600 860,630 760,648 C640,670 520,668 420,645 C280,612 140,540 0,500 Z" fill="var(--purple)"/>
      <path class="sweep-orange" d="M0,520 C130,560 280,630 420,660 C560,690 690,680 780,662 C880,640 980,612 1050,592 L1050,745 L0,745 Z" fill="var(--orange)"/>

      <!-- cover panel -->
      <path role="img" aria-label="Photo of a runner in a red jacket holding his knee on an open road" d="M700,242 C820,198 940,168 1050,158 L1050,568 C960,592 860,618 700,640 Z" fill="url(#roadTone)"/>
      <path class="cover-band-orange" d="M700,222 C820,165 940,128 1050,113 L1050,138 C940,150 820,185 700,234 Z" fill="var(--orange)"/>
      <path class="cover-band-purple" d="M700,236 C820,188 940,158 1050,146 L1050,160 C940,170 820,200 700,244 Z" fill="var(--purple)"/>

      <g role="img" aria-label="Circular photo of a woman's back facing a mirror">
        <circle cx="130" cy="528" r="82" fill="url(#mirrorTone)" stroke="var(--purple)" stroke-width="6"/>
      </g>
      <g role="img" aria-label="Circular photo of a group class holding a stretching pose on mats">
        <circle cx="946" cy="648" r="76" fill="url(#classTone)" stroke="var(--purple)" stroke-width="6"/>
      </g>
    </svg>

    <section class="panel panel-left">
      <h2 class="posture-title">What Does Your Posture<br>Reveal About You?</h2>
      <div class="posture-copy">
        <p>The easiest way to identify muscle compensation is to look for misalignments in your body. Stand in front of a full length mirror and take a look at your posture. Without making any adjustments, what obvious misalignments do you see?</p>
        <p>Place your hands on your waist line. Is one hip higher than the other? What about your feet? Does it feel like more of your weight is on one side? Does one foot turn out more? Now take a look at your shoulders. Is one higher than the other?</p>
        <p>If you answered yes to any of these questions, your pain is likely the result of muscle compensation and can benefit from the stride haven studio approach.</p>
      </div>
    </section>

    <section class="panel panel-middle">
      <div class="seminar-badge">
        <div class="seminar-badge-inner">
          <div class="seminar-free">FREE</div>
          <div class="seminar-name">INFORMATION<br>SEMINAR</div>
        </div>
      </div>
      <p class="slogan">feel better.<br>move better.<br>live better.</p>
      <div class="divider"></div>
      <p class="seminar-copy">To learn more about how to restore balance in your body, and for a <span class="highlight">FREE</span> posture assessment, sign up for our <span class="highlight">FREE information seminar.</span></p>
      <p class="reserve">Reserve your space online at<br><span class="url">www.stridehavenstudio.example</span></p>
      <div class="footer-brand"><span class="brand-square"></span><span>stridehavenstudio</span></div>
    </section>

    <section class="panel panel-right">
      <div class="header-brand"><span class="brand-square"></span><span>stridehavenstudio</span></div>
      <h1 class="cover-headline">Exercise<br>Your Pain Away<br>and Move Easier</h1>
    </section>
  </div>
</div>
</body>
</html>
```